Chinese citizens moving to SYDNEY!

We need an A5 size flier for our new business. We would like this to be a fold-out flyer (brochure-style, i.e. 4 sides - front cover, middle, back cover). Full colour print (or 4 colour if it can be done without compromising the look). We need two versions of the same flyer - one in Chinese and one in English. Same design and imagery, just different languages. Copy is attached with imagery (subject to change once we source high res images).

Target Market(s)

Chinese citizens looking to emigrate to Sydney AND Chinese citizens who have recently moved to Sydney.

Industry/Entity Type

Business

Font styles to use
Sans Serif

Colors
ec1f27
000000
ffffff
fece3e

Requirements
Must have
• The front cover of the flier must be clean looking and show just our business name and tag line, along with an image of Sydney Harbour (provided). Main information ideally to be spread across the 2 centre pages with the back page quite clean, but if the text is too small we could consider it being spread across the remaining 3 pages (i.e. centre of the brochure, then the back cover).
• We would like it to be a clean and easy to read design. Suggested colours are written in the brief.
• It would be ideal to have a designer who can read Mandarin so that they know which characters make up a headline, which characters should not be spaced over two rows of text etc.

```html
<!DOCTYPE html>
<html lang="en">
<head>
<meta charset="utf-8">
<title>Silver Wattle Concierge – Brochure</title>
<link rel="stylesheet" href="https://fonts.googleapis.com/css2?family=Source+Sans+3:wght@300;400;600;700&display=swap">
<style>
  :root{
    --gold:#d9a42a;
    --gold-light:#e7b640;
    --ink:#1d1d1d;
    --paper:#f3f3f3;
    --canvas:#5f5f5f;
    --text:#2b2b2b;
  }
  *{box-sizing:border-box;margin:0;padding:0}
  html,body{width:890px;height:1200px;overflow:hidden}
  body{background:var(--canvas);font-family:"Source Sans 3",Arial,sans-serif;color:var(--text);position:relative}
  .spread{position:absolute;left:79px;width:842px;height:594px;background:var(--paper);
    transform:scale(.856);transform-origin:top left;overflow:hidden}
  .spread--outer{top:68px}
  .spread--inner{top:625px}
  .spread svg.art{position:absolute;inset:0;width:842px;height:594px}
  .fold{position:absolute;top:0;left:391px;width:60px;height:594px;
    background:linear-gradient(90deg,rgba(0,0,0,0) 0,rgba(0,0,0,.10) 48%,rgba(255,255,255,.12) 52%,rgba(0,0,0,0) 100%);pointer-events:none}

  /* back cover */
  .contact{position:absolute;left:0;width:421px;top:502px;text-align:center;font-size:9.5px;line-height:12px;color:var(--ink)}
  .contact__cta{color:var(--gold);margin-bottom:14px}
  .contact__web{color:var(--gold);margin-top:10px}
  /* front cover */
  .cover-title{position:absolute;left:421px;width:421px;top:520px;text-align:center}
  .cover-title__name{font-weight:300;font-size:23px;color:var(--gold);line-height:30px}
  .cover-title__tag{font-weight:400;font-size:19px;color:var(--ink);line-height:26px;margin-top:3px}

  /* inner pages */
  .about{position:absolute;left:18px;top:230px;width:384px;font-size:9.2px;line-height:10px;text-align:justify;color:var(--text)}
  .about__heading{font-size:12px;font-weight:400;color:var(--ink);padding-bottom:3px;border-bottom:1px solid var(--gold);margin-bottom:6px;text-align:left}
  .about p{margin-bottom:10px}
  .about p.about__lead-in{margin-bottom:0;color:var(--ink)}

  .service-label{position:absolute;height:16px;padding-left:18px;width:146px;
    background:var(--gold);color:#fff;font-weight:600;font-size:11.5px;line-height:16px;
    clip-path:polygon(0 0,100% 0,94% 100%,0 100%)}
  .service-list{position:absolute;list-style:none;font-size:9.2px;line-height:12px;color:var(--text)}
  .service-list li{position:relative;padding-left:12px}
  .service-list li::before{content:"";position:absolute;left:1px;top:3.5px;width:5px;height:5px;border-radius:50%;
    background:var(--gold-light);box-shadow:0 0 0 1px #f6d27a inset}
  .col-left{left:19px;width:384px;text-align:justify}
  .col-right{left:441px;width:392px}
  .col-right.list-health{line-height:11.6px}
</style>
</head>
<body>

<section class="spread spread--outer">
  <svg class="art" viewBox="0 0 842 594" preserveAspectRatio="none">
    <defs>
      <linearGradient id="harbourSky" x1="0" y1="0" x2="1" y2="1">
        <stop offset="0" stop-color="#2c3440"/>
        <stop offset=".35" stop-color="#4d7fb8"/>
        <stop offset=".65" stop-color="#8fb6e0"/>
        <stop offset=".85" stop-color="#e8b7a8"/>
        <stop offset="1" stop-color="#c58a5a"/>
      </linearGradient>
      <linearGradient id="band" x1="0" y1="0" x2="1" y2="0">
        <stop offset="0" stop-color="#111"/>
        <stop offset=".5" stop-color="#2a2a2a"/>
        <stop offset="1" stop-color="#0a0a0a"/>
      </linearGradient>
    </defs>
    <rect class="harbour-photo" role="img" aria-label="Photograph of Sydney Harbour Bridge at dusk with the city skyline" x="0" y="0" width="842" height="480" fill="url(#harbourSky)"/>
    <path class="wave-band" fill="url(#band)"
      d="M0,252 C70,212 210,228 330,300 C450,372 540,462 650,458 C730,452 800,405 842,372
         L842,418 C760,482 660,522 560,506 C470,494 420,470 330,446 C230,420 100,440 0,532 Z"/>
    <path fill="none" stroke="#d9a42a" stroke-width="3"
      d="M842,418 C760,482 660,522 560,506 C470,494 420,470 330,446 C230,420 100,440 0,532"/>
    <path fill="none" stroke="#d9a42a" stroke-width="1.5"
      d="M650,458 C730,452 800,405 842,372"/>
  </svg>
  <div class="fold"></div>

  <div class="contact">
    <p class="contact__cta">Contact us today to discuss how we can serve you!</p>
    <p>Phone: (555) 014-2378</p>
    <p>Email: hello@silverwattleconcierge.com</p>
    <p class="contact__web">www.silverwattleconcierge.example</p>
  </div>

  <div class="cover-title">
    <h1 class="cover-title__name">Silver Wattle Concierge</h1>
    <p class="cover-title__tag">Sydney’s Relocation and Settlement Experts</p>
  </div>
</section>

<section class="spread spread--inner">
  <svg class="art" viewBox="0 0 842 594" preserveAspectRatio="none">
    <defs>
      <linearGradient id="familyPhoto" x1="0" y1="0" x2="1" y2="1">
        <stop offset="0" stop-color="#a9c9e6"/>
        <stop offset=".5" stop-color="#d8e6f2"/>
        <stop offset="1" stop-color="#4d86b4"/>
      </linearGradient>
      <linearGradient id="schoolPhoto" x1="0" y1="0" x2="1" y2="0">
        <stop offset="0" stop-color="#1e2420"/>
        <stop offset=".5" stop-color="#59605c"/>
        <stop offset="1" stop-color="#c8ccd0"/>
      </linearGradient>
      <linearGradient id="housePhoto" x1="0" y1="0" x2="0" y2="1">
        <stop offset="0" stop-color="#3b4a6a"/>
        <stop offset="1" stop-color="#c98a4a"/>
      </linearGradient>
      <linearGradient id="footBand" x1="0" y1="0" x2="1" y2="0">
        <stop offset="0" stop-color="#0b0b0b"/>
        <stop offset=".5" stop-color="#2b2b2b"/>
        <stop offset="1" stop-color="#0b0b0b"/>
      </linearGradient>
    </defs>
    <path role="img" aria-label="Photograph of a smiling family playing at the beach"
      fill="url(#familyPhoto)" d="M0,0 H421 V142 C300,146 140,160 0,182 Z"/>
    <path fill="#111" d="M0,182 C140,160 300,146 421,142 L421,152 C300,156 140,172 0,196 Z"/>
    <path fill="none" stroke="#d9a42a" stroke-width="2.5" d="M0,196 C140,172 300,156 421,152"/>
    <path role="img" aria-label="Photograph of schoolgirls in uniform outdoors"
      fill="url(#schoolPhoto)" d="M421,0 H842 V92 C700,92 560,100 421,110 Z"/>
    <path fill="#111" d="M421,110 C560,100 700,92 842,92 L842,104 C700,104 560,112 421,122 Z"/>
    <path fill="none" stroke="#d9a42a" stroke-width="2.5" d="M421,122 C560,112 700,104 842,104"/>
    <circle cx="778" cy="114" r="54" fill="#d9a42a"/>
    <circle cx="778" cy="114" r="49" fill="url(#housePhoto)" role="img" aria-label="Photograph of a modern family home at dusk"/>
    <path fill="url(#footBand)" d="M0,549 C250,552 600,566 842,570 V594 H0 Z"/>
  </svg>
  <div class="fold"></div>

  <div class="about">
    <h2 class="about__heading">ABOUT US</h2>
    <p>Silver Wattle Concierge is a premium lifestyle service supporting families who are planning or currently migrating to and investing in Australia. Specialising in the city of Sydney, Silver Wattle Concierge helps families to feel comfortable and at home as soon as possible. Our team of local experts provide support every step of the way – answering questions, providing advice and breaking down the language barrier.</p>
    <p>Our services are highly customisable to suit the needs of individual families. Whether it’s finding the best school for your children, the help you need in your home, knowing where to buy your favourite groceries or an introduction to a great GP or Specialist – Silver Wattle Concierge will cater to your every need. Your family will be assigned a professional Personal Assistant who is fluent in both English and Mandarin, making the process of migrating less daunting and more enjoyable.</p>
    <p class="about__lead-in">Our services include but are not limited to:</p>
  </div>

  <div class="service-label" style="left:0;top:395px">SCHOOL</div>
  <ul class="service-list col-left" style="top:413px">
    <li>Recommend the best schools and childcare centres</li>
    <li>Compare school rankings and academic results</li>
    <li>Arrange private tours of schools and meetings with Principals</li>
    <li>Manage the school application process through to completion</li>
    <li>Assist with starting school, such as purchase of uniforms and textbooks, understanding school procedures and more</li>
    <li>Appoint private tutors to assist with learning English and completing homework assignments</li>
    <li>Organise extra curricular activities, such as piano lessons, tennis lessons and more</li>
    <li>Translate all school correspondence such as academic report cards, homework assignments and more</li>
  </ul>

  <div class="service-label" style="left:421px;top:153px">HOME &amp; CAR</div>
  <ul class="service-list col-right" style="top:172px">
    <li>Recommend the best suburbs for families</li>
    <li>Make introductions to Real Estate Agents and support the buying process</li>
    <li>Arrange unpacking and home organisation services</li>
    <li>Assist to purchase furniture and appliances</li>
    <li>Source the best utility companies and organise connection – electricity, gas, water, phone, internet, TV and more</li>
    <li>Appoint staff for your home such as cleaners, gardeners and more</li>
    <li>Compare home insurance options and assist with purchasing</li>
    <li>Assist with car purchasing, leasing and acquiring necessary insurance</li>
  </ul>

  <div class="service-label" style="left:421px;top:290px">EVERYDAY NECESSITIES</div>
  <ul class="service-list col-right" style="top:309px">
    <li>Explain local grocery options such as supermarkets, specialty stores, Asian grocers and more</li>
    <li>Recommend beauty and wellness services such as hair salons, nail parlours, beauty salons and more</li>
    <li>Explain retail shopping options such major shopping centres and luxury brands</li>
    <li>Source quality trades people such as plumbers, electricians, painters and more</li>
    <li>Assist with government registrations such as drivers license, Medicare and more</li>
    <li>Assist to open bank accounts and set up online banking</li>
    <li>Assist to set up memberships – library, gym, golf club and more</li>
    <li>Explain private and public transport options</li>
    <li>Organise private and group language classes</li>
    <li>Translate documents and mail</li>
  </ul>

  <div class="service-label" style="left:421px;top:446px">Health &amp; Lifestyle</div>
  <ul class="service-list col-right list-health" style="top:464px">
    <li>Compare health insurance options</li>
    <li>Recommend the best medical professionals – GP, Dentist, Acupuncture and more</li>
    <li>Recommend restaurants</li>
    <li>Suggest the best local parks to visit and other outdoor activities</li>
    <li>Explain local dangers such as Australian wildlife, beach safety and more</li>
    <li>Suggest family outings, recommend holiday destinations, plan children’s birthday parties, play dates and more</li>
    <li>Arrange Private chauffeurs</li>
  </ul>
</section>

</body>
</html>
```